Drawing Book Cover

I need a design for my Drawing Book which selling to Primary School and Secondary children. Following are the size and description.

Size: 15" x 11" (381mm x 280mm) Landscape.
I would like to see designs that use Black color only as the book cover will using Kraft Paper.

School

```html
<!DOCTYPE html>
<html lang="en">
<head>
<meta charset="UTF-8">
<title>My Drawing Book – Cover Spread</title>
<link href="https://fonts.googleapis.com/css2?family=Alfa+Slab+One&family=Encode+Sans+Condensed:wght@300&display=swap" rel="stylesheet">
<style>
  :root {
    --page: #ffffff;
    --kraft-light: #c29d66;
    --kraft-mid: #b8915a;
    --kraft-dark: #a9834d;
    --ink: #2b2418;
    --mark: #000000;
    --label: #111111;
  }
  * { margin: 0; padding: 0; box-sizing: border-box; }
  html, body {
    width: 1200px;
    height: 1000px;
    overflow: hidden;
    background: var(--page);
  }
  .spread {
    position: relative;
    width: 1200px;
    height: 1000px;
  }
  .kraft-sheet {
    position: absolute;
    left: 14px;
    top: 280px;
    width: 1176px;
    height: 440px;
    background:
      radial-gradient(ellipse at 30% 40%, var(--kraft-light), transparent 60%),
      radial-gradient(ellipse at 75% 65%, var(--kraft-light), transparent 55%),
      linear-gradient(135deg, var(--kraft-mid), var(--kraft-dark));
  }
  .crop-marks {
    position: absolute;
    left: 0;
    top: 0;
  }
  .title {
    position: absolute;
    font-family: "Alfa Slab One", serif;
    color: var(--ink);
    text-align: center;
    line-height: 1;
    white-space: nowrap;
    transform: translateX(-50%);
  }
  .title .title-my { display: block; }
  .title .title-name { display: block; }

  .title--back { left: 145px; top: 350px; }
  .title--back .title-my { font-size: 33px; }
  .title--back .title-name { font-size: 21px; margin-top: 2px; }

  .title--front { left: 912px; top: 418px; }
  .title--front .title-my { font-size: 78px; }
  .title--front .title-name { font-size: 49px; margin-top: 2px; }

  .panel-label {
    position: absolute;
    font-family: "Encode Sans Condensed", sans-serif;
    font-weight: 300;
    font-size: 24px;
    color: var(--label);
    transform: translateX(-50%);
  }
  .panel-label--back { left: 389px; top: 738px; }
  .panel-label--front { left: 897px; top: 743px; }
</style>
</head>
<body>
  <main class="spread">
    <div class="kraft-sheet" role="img" aria-label="Crumpled brown kraft paper texture covering the full cover spread"></div>

    <svg class="crop-marks" width="1200" height="1000" viewBox="0 0 1200 1000" aria-hidden="true">
      <g stroke="var(--mark)" stroke-width="1.5">
        <line x1="20" y1="255" x2="20" y2="277"/>
        <line x1="601" y1="255" x2="601" y2="277"/>
        <line x1="1181" y1="255" x2="1181" y2="277"/>
        <line x1="20" y1="722" x2="20" y2="744"/>
        <line x1="601" y1="722" x2="601" y2="744"/>
        <line x1="1181" y1="722" x2="1181" y2="744"/>
        <line x1="0" y1="285" x2="10" y2="285"/>
        <line x1="0" y1="713" x2="10" y2="713"/>
        <line x1="1190" y1="285" x2="1200" y2="285"/>
        <line x1="1190" y1="713" x2="1200" y2="713"/>
      </g>
    </svg>

    <h2 class="title title--back">
      <span class="title-my">my</span>
      <span class="title-name">Drawing Book</span>
    </h2>

    <h1 class="title title--front">
      <span class="title-my">my</span>
      <span class="title-name">Drawing Book</span>
    </h1>

    <p class="panel-label panel-label--back">Back</p>
    <p class="panel-label panel-label--front">Front</p>
  </main>
</body>
</html>
```